Thai Restaurant Billboard Design

Design a billboard promoting food delivery during this Coronavirus time. We want to grab attention by embracing the Coronavirus and offering food delivery. People are sitting at home and this is the right time to promote food delivery.

I have the logo and spec sheet attached.

Target Market(s)

Anyone.

Requirements
Must have
• Top Heading should be big and bold:

Coronavirus Got You Quarantined?

Then put under

We Deliver
Healthy Thai Food!
Put the logo that is attached
555-231-0164
Nice to have
• Eyecatching. Creative.
Should not have
• Don't have any not haves. Make it look good.

```html
<!DOCTYPE html>
<html lang="en">
<head>
<meta charset="UTF-8">
<title>Thai Delivery Billboard</title>
<link href="https://fonts.googleapis.com/css2?family=Montserrat:wght@400;500;700;800&display=swap" rel="stylesheet">
<style>
  :root {
    --page-bg: #dfe3e8;
    --board-bg: #ececec;
    --ink: #1f1f1f;
    --accent: #f7c600;
    --band: #242424;
    --white: #ffffff;
  }
  * { box-sizing: border-box; margin: 0; padding: 0; }
  html, body {
    width: 1200px; height: 780px; overflow: hidden;
    background: var(--page-bg);
    font-family: "Montserrat", Arial, sans-serif;
  }
  .billboard {
    position: absolute; left: 0; top: 183px;
    width: 1200px; height: 414px;
    background: radial-gradient(ellipse at 50% 45%, #f4f4f4 0%, var(--board-bg) 70%, #e2e2e2 100%);
    overflow: hidden;
  }
  .food-photo { position: absolute; }
  .food-photo--left {
    left: 0; top: 0; width: 190px; height: 414px;
    background:
      radial-gradient(circle at 40% 20%, rgba(143,174,106,.55), transparent 45%),
      radial-gradient(circle at 35% 60%, rgba(230,225,210,.9), transparent 30%),
      radial-gradient(circle at 55% 88%, rgba(201,115,58,.75), transparent 32%),
      linear-gradient(90deg, rgba(120,125,130,.45), rgba(236,236,236,0));
  }
  .food-photo--right {
    left: 935px; top: 0; width: 265px; height: 414px;
    background:
      radial-gradient(circle at 45% 30%, rgba(201,115,58,.85), transparent 36%),
      radial-gradient(circle at 85% 38%, rgba(143,174,106,.7), transparent 16%),
      radial-gradient(circle at 70% 80%, rgba(201,115,58,.85), transparent 38%),
      linear-gradient(270deg, rgba(217,214,210,.6), rgba(236,236,236,0));
  }
  .headline-main {
    position: absolute; left: 226px; top: 46px;
    font-size: 82px; font-weight: 800; color: var(--ink);
    letter-spacing: -1.5px; line-height: 1;
  }
  .headline-sub {
    position: absolute; left: 345px; top: 136px;
    display: flex; align-items: baseline; gap: 14px;
    line-height: 1;
  }
  .headline-sub__lead { font-size: 31px; font-weight: 800; color: var(--ink); }
  .headline-sub__key { font-size: 53px; font-weight: 800; color: var(--accent); letter-spacing: -.5px; }
  .accent-strokes { position: absolute; left: 0; top: 0; }
  .delivery-band {
    position: absolute; left: 508px; top: 240px;
    width: 452px; height: 48px;
    background: var(--band);
    display: flex; align-items: center; justify-content: center; gap: 12px;
    font-size: 23px; white-space: nowrap;
  }
  .delivery-band__lead { color: var(--accent); font-weight: 500; }
  .delivery-band__claim { color: var(--white); font-weight: 800; }
  .phone {
    position: absolute; left: 524px; top: 300px;
    font-size: 60px; font-weight: 500; color: var(--ink);
    letter-spacing: 2px; line-height: 1; white-space: nowrap;
  }
  .brand-name {
    position: absolute; left: 226px; top: 330px; width: 300px;
    text-align: center; color: var(--ink); line-height: 1.15;
    font-weight: 700; white-space: nowrap;
  }
  .brand-name__main { display: block; font-size: 22px; }
  .brand-name__sub { display: block; font-size: 17px; }
</style>
</head>
<body>
  <main class="billboard">
    <div class="food-photo food-photo--left" role="img" aria-label="Overhead photo of chopped vegetables on a board, a dip bowl and a bowl of Thai stir-fry"></div>
    <div class="food-photo food-photo--right" role="img" aria-label="Overhead photo of bowls of spiced sweet potato wedges with toppings, lime and guacamole"></div>

    <svg class="accent-strokes" width="1200" height="414" viewBox="0 0 1200 414" aria-hidden="true">
      <g stroke="var(--accent)" stroke-width="2.5" stroke-linecap="round" fill="none">
        <line x1="842" y1="66" x2="864" y2="36"/>
        <line x1="846" y1="76" x2="870" y2="64"/>
        <line x1="852" y1="88" x2="887" y2="88"/>
        <line x1="293" y1="150" x2="330" y2="150"/>
        <line x1="298" y1="160" x2="330" y2="158"/>
        <line x1="318" y1="195" x2="334" y2="170"/>
      </g>
    </svg>

    <h1 class="headline-main">Coronavirus</h1>
    <p class="headline-sub">
      <span class="headline-sub__lead">Got You</span>
      <span class="headline-sub__key">Quarantined?</span>
    </p>

    <p class="brand-name">
      <span class="brand-name__main">Siam Orchid Kitchen</span>
      <span class="brand-name__sub">Restaurant</span>
    </p>

    <p class="delivery-band">
      <span class="delivery-band__lead">We Deliver</span>
      <span class="delivery-band__claim">Healthy Thai Food!</span>
    </p>
    <p class="phone">555-231-0164</p>
  </main>
</body>
</html>
```